Business Card Upgrade

I have designed our business card using our new logo. I think it needs imporovements. We used to have two cards for our business. One card was for our software business, and the other was for our consulting business. We are now in the process of combining our websites, marketing, name, and a new logo.

Our goal is to have a really sharp professional logo. One reason I designed the card the way I did was that our Titles are sometimes long, and by separating the person's name and title, it shows up very well and the title can be adjusted no matter how long it is. Sometimes the title can be 4 or 5 words or more.

We really like our logo on black as it shows up very nice. Our PMS colors are as follows: 368C and 459C.

The Designer that will be working with us will need to deliver the following:

The front and back of the Business Card Design will need to be delivered in a high quality JPEG, and
The front and back of the Business Card Design in Illustrator Format .ai
Any fonts will need to be sent to us if they are not standard and are required to open the Illustrator file correctly.

To help us get a good idea of the card with a title, please use the title: " Director of Software Development "

NOTE: The chosen designer will be selected to design our new letterhead within 2 weeks from the closing of this contest.
Updates

To help us make sure the card design works with longer titles, please use the followign job title on the card:  

"Director of Software and Product Development"

 

ALL DESIGNERS:

1. I appreciate the different angles you are showing the cards, but please be sure and always show the direct view, so I can see the layout and what the person I hand the card will see.

2. Please do not use white.  Please use off white as I don't care for white cards and they get dirty easy and do not represent the designs well.

Dear Designers,

Please provide samples straight one as a viewer of the card will see.  Some of the angles that are presented make it impossible to tell how everything fits, and sometimes even makes areas look skewed. So, please provide a straight sample view.

Target Market(s)

Keystone 400 company executives such as Vice Presidents, and Directors

Industry/Entity Type

Software

Requirements
Must have
• Professional looking Card.

Our customers are Directors, Vice Presidents, and Presidents of companies as large as Keystone 400 companies. The card needs to get attention wile still looking professional.

Delivery of the finished product in Illustrator Format with any fonts needed to edit the text or open the file.

The card will be a heavy stock with a soft touch coating for that silk feel.

```html
<!DOCTYPE html>
<html lang="en">
<head>
<meta charset="utf-8">
<title>Harborline Trade Systems – Business Card</title>
<link href="https://fonts.googleapis.com/css2?family=Montserrat:wght@700&family=Oswald:wght@400;500&family=Open+Sans:wght@400&display=swap" rel="stylesheet">
<style>
  :root{
    --page:#e9e6e0;
    --card-dark:#121212;
    --card-mid:#262626;
    --green:#5cb81f;
    --green-deep:#3f8a12;
    --gold:#d8c98c;
    --text-light:#ece8dc;
  }
  *{margin:0;padding:0;box-sizing:border-box}
  html,body{width:1200px;height:1024px;overflow:hidden;background:var(--page)}
  .sheet{width:1200px;height:1024px;display:flex;flex-direction:column;align-items:center;justify-content:center;gap:64px}
  .card{position:relative;width:700px;height:400px;overflow:hidden;
    background:radial-gradient(ellipse at 45% 40%,var(--card-mid) 0%,var(--card-dark) 70%);
    box-shadow:0 10px 28px rgba(0,0,0,.25)}
  .band{position:absolute;left:0;right:0;bottom:0;height:56px;background:var(--green);
    border-top:3px solid var(--green-deep)}
  .wordmark{font-family:"Montserrat",sans-serif;font-weight:700;color:var(--green);
    text-transform:uppercase;line-height:1.05}
  /* front */
  .front .wordmark{position:absolute;left:44px;top:52px;font-size:30px;letter-spacing:1px}
  .rule{position:absolute;left:44px;top:156px;width:410px;height:2px;background:var(--gold)}
  .rule::after{content:"";position:absolute;left:0;top:-18px;width:2px;height:38px;background:var(--gold)}
  .person{position:absolute;left:472px;top:140px;width:196px}
  .person-name{font-family:"Oswald",sans-serif;font-weight:500;font-size:26px;color:var(--green);
    text-transform:uppercase;letter-spacing:.5px;line-height:1;white-space:nowrap}
  .person-title{font-family:"Oswald",sans-serif;font-weight:400;font-size:16px;line-height:1.35;
    color:var(--text-light);margin-top:10px}
  .contacts{position:absolute;left:60px;top:196px;list-style:none}
  .contacts li{display:flex;align-items:center;gap:14px;height:32px;
    font-family:"Open Sans",sans-serif;font-size:16px;color:var(--text-light)}
  .contacts svg{width:14px;height:14px;fill:var(--green);flex:none}
  /* back */
  .back .wordmark{position:absolute;left:0;right:0;top:112px;text-align:center;font-size:48px;letter-spacing:2px}
  .tagline{position:absolute;left:0;right:0;bottom:0;height:56px;display:flex;align-items:center;justify-content:center;
    font-family:"Oswald",sans-serif;font-weight:400;font-size:19px;letter-spacing:1.5px;color:#1d3a08;text-transform:uppercase}
</style>
</head>
<body>
<main class="sheet">
  <section class="card front" aria-label="Card front">
    <div class="wordmark">Harborline<br>Trade Systems</div>
    <div class="rule"></div>
    <div class="person">
      <div class="person-name">Dana Whitfield</div>
      <div class="person-title">Director of Software and Product Development</div>
    </div>
    <ul class="contacts">
      <li><svg viewBox="0 0 24 24"><path d="M6.6 10.8a15 15 0 0 0 6.6 6.6l2.2-2.2a1 1 0 0 1 1-.25 11.4 11.4 0 0 0 3.6.57 1 1 0 0 1 1 1V20a1 1 0 0 1-1 1A17 17 0 0 1 3 4a1 1 0 0 1 1-1h3.5a1 1 0 0 1 1 1c0 1.25.2 2.450.57 3.57a1 1 0 0 1-.25 1z"/></svg>555.018.2740</li>
      <li><svg viewBox="0 0 24 24"><path d="M2 5h20v14H2zm2 2v.5l8 5 8-5V7z"/></svg>dana@harborlinetrade.com</li>
      <li><svg viewBox="0 0 24 24"><circle cx="12" cy="12" r="10"/></svg>www.harborlinetrade.com</li>
      <li><svg viewBox="0 0 24 24"><path d="M12 2a7 7 0 0 0-7 7c0 5 7 13 7 13s7-8 7-13a7 7 0 0 0-7-7zm0 9.5A2.5 2.5 0 1 1 12 6.5a2.5 2.5 0 0 1 0 5z"/></svg>418 Lantern Bay Road Marlow, AL 36000</li>
    </ul>
    <div class="band"></div>
  </section>

  <section class="card back" aria-label="Card back">
    <div class="wordmark">Harborline<br>Trade Systems</div>
    <div class="band"></div>
    <div class="tagline">Consulting &nbsp;Software &nbsp;Operations &nbsp;Administration</div>
  </section>
</main>
</body>
</html>
```